Agricultural Consulting Website

Provide a modern yet business like website for my new Agriculture Consulting Business in Australia called FenTrove. Whilst we are based in Australia we are targetting both domestic and international markets (especially in Asia). We are targetting corporate, small business, government and farmer clients. The design should compliment our logo also sourced through pixel guild. The webiste should be easy for me to keep updated on a regular basis without the need to go back to the designer.

Industry/Entity Type

Business

Requirements
Must have
• clean crisp feel
• be modern yet business like
• be able to be updated by myself easily

```html
<!DOCTYPE html>
<html lang="en">
<head>
<meta charset="utf-8">
<title>FenTrove – Agriculture Consultancy</title>
<link href="https://fonts.googleapis.com/css2?family=PT+Sans:ital,wght@0,400;0,700;1,400;1,700&display=swap" rel="stylesheet">
<style>
:root{
  --green:#5a9410;
  --green-dark:#3f6e08;
  --green-light:#79b821;
  --brown:#6b3a12;
  --nav-dark:#2b221d;
  --nav-mid:#3a302a;
  --band:#f2f2f2;
  --card:#f1f1f1;
  --text:#555;
  --heading:#3a3a3a;
  --footer:#2c221d;
  --footer-strip:#cfcbc8;
  --sky:#6aa6e0;
  --grass:#7cc03c;
}
*{margin:0;padding:0;box-sizing:border-box}
html,body{width:1200px;height:943px;overflow:hidden;background:#fff}
body{position:relative;font-family:'PT Sans',sans-serif;color:var(--text)}
.hero-backdrop{position:absolute;left:0;top:0;width:1200px;height:473px;
  background:
   radial-gradient(ellipse 420px 120px at 600px 80px,rgba(255,255,255,.95),rgba(255,255,255,0) 70%),
   linear-gradient(180deg,#b9c3a6 0%,#8a9c72 12%,#d9d3a0 30%,#c9c23a 50%,#a6ad22 65%,#4b7a1c 85%,#2d5a14 100%)}
.brand{position:absolute;left:0;top:34px;width:1200px;text-align:center}
.brand-name{display:inline-flex;align-items:center;gap:10px;font-size:38px;font-weight:400;color:var(--green);line-height:1}
.brand-mark{width:48px;height:48px;background:var(--brown)}
.tagline{position:absolute;left:0;top:98px;width:1200px;text-align:center;font-size:13px;font-style:italic;font-weight:700;color:var(--brown)}
.main-nav{position:absolute;left:171px;top:129px;width:859px;height:47px;
  background:linear-gradient(180deg,var(--nav-mid),var(--nav-dark));
  box-shadow:0 2px 6px rgba(0,0,0,.4);display:flex;justify-content:space-around;align-items:center;padding:0 22px}
.main-nav a{color:#bfb8b2;text-decoration:none;font-size:11px;letter-spacing:2px;text-transform:uppercase}
.main-nav a.active{color:#fff}
.slider{position:absolute;left:171px;top:176px;width:858px;height:297px;
  background:linear-gradient(180deg,var(--sky) 0%,#cfe3f5 45%,#eef4f8 62%,var(--grass) 68%,#5ea12b 100%);
  box-shadow:0 0 10px rgba(0,0,0,.35)}
.slider-arrow{position:absolute;top:305px;width:14px;height:30px}
.slider-arrow.prev{left:144px}
.slider-arrow.next{left:1045px}
.intro{position:absolute;left:0;top:473px;width:1200px;height:96px;background:var(--band);border-bottom:1px solid #e2e2e2}
.intro h1{position:absolute;left:206px;top:17px;font-size:18px;font-weight:400;color:var(--heading);letter-spacing:.3px}
.intro p{position:absolute;left:206px;top:46px;width:560px;font-size:11px;line-height:17px;color:#666}
.btn{position:absolute;display:flex;align-items:center;justify-content:center;
  background:linear-gradient(180deg,var(--green-light),var(--green));
  border:2px solid var(--green-dark);color:#fff;font-weight:700;text-transform:uppercase;letter-spacing:1px;
  text-shadow:0 1px 1px rgba(0,0,0,.35);text-decoration:none;box-shadow:0 4px 4px -2px rgba(0,0,0,.15)}
.btn-learn{left:793px;top:26px;width:200px;height:41px;font-size:14px}
.feature{position:absolute;top:594px;width:249px;height:188px;background:var(--card);box-shadow:0 1px 3px rgba(0,0,0,.2)}
.feature-photo{height:121px;border-bottom:4px solid #ddd}
.feature h2{margin:10px 0 0 9px;font-size:12px;font-weight:700;color:var(--heading);letter-spacing:.5px}
.feature p{margin:6px 9px 0;font-size:9px;line-height:14px;color:#555}
.f1{left:206px}.f2{left:476px}.f3{left:746px}
.f1 .feature-photo{background:linear-gradient(180deg,#9cc456,#5f9a2a)}
.f2 .feature-photo{background:linear-gradient(180deg,#4b8fd8 0%,#b7d3ea 50%,#7ea34a 70%,#c8302a 100%)}
.f3 .feature-photo{background:radial-gradient(circle at 40% 30%,#fff3b0,#d9b04a 60%,#7a5a2a)}
.btn-more{top:795px;width:86px;height:32px;font-size:12px}
.m1{left:286px}.m2{left:557px}.m3{left:826px}
.footer-strip{position:absolute;left:0;top:874px;width:1200px;height:10px;background:var(--footer-strip)}
.site-footer{position:absolute;left:0;top:884px;width:1200px;height:59px;background:var(--footer);font-size:9.5px;color:#a59c95;letter-spacing:.5px}
.copyright{position:absolute;left:206px;top:23px}
.copyright strong{color:#fff;font-weight:400}
.footer-nav{position:absolute;right:205px;top:23px;display:flex;gap:22px}
.footer-nav a{color:#a59c95;text-decoration:none}
.footer-nav a.active{color:#fff}
</style>
</head>
<body>
<div class="hero-backdrop" role="img" aria-label="Blurred photo of a golden crop field under a cloudy sky"></div>

<header>
  <div class="brand"><span class="brand-name"><span class="brand-mark"></span>FenTrove</span></div>
  <div class="tagline">Domestic &amp; international Agriculture Consultancy</div>
</header>

<nav class="main-nav">
  <a class="active" href="#">Home</a>
  <a href="#">About</a>
  <a href="#">Activites</a>
  <a href="#">Events</a>
  <a href="#">Members</a>
  <a href="#">Positions Vacant</a>
  <a href="#">Blog</a>
  <a href="#">Contact</a>
</nav>

<div class="slider" role="img" aria-label="Photo of a smiling farmer with arms crossed in front of red barns on green pasture under a blue sky"></div>
<svg class="slider-arrow prev" viewBox="0 0 14 30"><path d="M10 2 L4 15 L10 28" fill="none" stroke="#d8d4b8" stroke-width="2"/></svg>
<svg class="slider-arrow next" viewBox="0 0 14 30"><path d="M4 2 L10 15 L4 28" fill="none" stroke="#d8d4b8" stroke-width="2"/></svg>

<section class="intro">
  <h1>LOREM IPSUM DOLOR SIT AMET, CONSECTETUR ADIPISCING ELIT VIVAM</h1>
  <p>Etur adipiscing elit. Vivamus tincidunt, odio ac fermentum vehicula, urna nisl lacinia mauris, in vehicula eros mauris at mi. Praesent orci lorem, congue tempus molestie vel, fringilla non erat. Nunc nec neque</p>
  <a class="btn btn-learn" href="#">Learn More</a>
</section>

<article class="feature f1">
  <div class="feature-photo" role="img" aria-label="Photo of a tractor pulling hay bales along a green field track"></div>
  <h2>LOREM IPSUM DOLOR</h2>
  <p>Etur adipiscing elit. Vivamus tincidunt, odio ac ferme tum vehicula, urna nisl lacinia mauris, in vehicula ero</p>
</article>
<article class="feature f2">
  <div class="feature-photo" role="img" aria-label="Photo of a worker in red overalls and yellow hard hat looking over green fields"></div>
  <h2>LOREM IPSUM DOLOR</h2>
  <p>Etur adipiscing elit. Vivamus tincidunt, odio ac ferme tum vehicula, urna nisl lacinia mauris, in vehicula ero</p>
</article>
<article class="feature f3">
  <div class="feature-photo" role="img" aria-label="Photo of seed heads backlit by warm golden sunlight"></div>
  <h2>LOREM IPSUM DOLOR</h2>
  <p>Etur adipiscing elit. Vivamus tincidunt, odio ac ferme tum vehicula, urna nisl lacinia mauris, in vehicula ero</p>
</article>

<a class="btn btn-more m1" href="#">More</a>
<a class="btn btn-more m2" href="#">More</a>
<a class="btn btn-more m3" href="#">More</a>

<div class="footer-strip"></div>
<footer class="site-footer">
  <div class="copyright">Copyright © 2013 &nbsp;<strong>Company Name</strong> &nbsp;| All rights reserved</div>
  <nav class="footer-nav">
    <a class="active" href="#">Home</a>
    <a href="#">About</a>
    <a href="#">Blog</a>
    <a href="#">Contact</a>
  </nav>
</footer>
</body>
</html>
```